KESTRA FLOW SUPPLY business card

We need a new business card for our company "Kestra Flow Supply". The company is very simple, we supply bulk heated water to the oilfield and industry. I have included a few images of cards that I like so that you have an idea of the direction I want to go. I will leave fonts up to the designer. I have also included our logo.
Updates

Hello Designers,  if there are any more submissions coming in you might consider using other background colors than black.  I am looking for a little bit of variety before making the decision.

Thanks,

Dale

Sorry, I meant to say background colors other than just black and white.

Thanks,

Dale

Target Market(s)

Ages 20 to 60. Oilfield consultants and Oil and Gas Companies

Industry/Entity Type

Business

Font styles to use
Sans Serif

Requirements
Must have
• Dale Fenwick

email info@kestraflowsupply.example

Phone # 555-318-2047
Fax 555-376-9150

Site 713, Box 2, Comp 4, RR3
Ashford Bend, XK, X9Z 4Q8

3-17-52-4 W4M
Hwy 905 Between RR37 & RR38

**Must have our logo

Nice to have
• Would be nice to have " Bulk Heated Water" somewhere on the card

The logo with the flame large across the background might look ok? The name of the company is KESTRA FLOW SUPPLY, but it probably isn't necessary to have the hot water under the logo all the time if you decide it looks better. As long as it is included somewhere on the card. The style of the KESTRA can change slightly (ie:; can be slanted).

The colors of the logo can change, but it might be nice to have the original color and logo somewhere small (corner?)

```html
<!DOCTYPE html>
<html lang="en">
<head>
<meta charset="utf-8">
<title>Kestra Flow Supply – Business Card</title>
<link href="https://fonts.googleapis.com/css2?family=Arimo:wght@400;700&display=swap" rel="stylesheet">
<style>
  :root {
    --stage-center: #ffffff;
    --stage-edge: #e4e5e6;
    --slate: #3d3d3d;
    --slate-light: #4a4a4a;
    --red-top: #e92027;
    --red-bottom: #c8161c;
    --ink-light: #ffffff;
    --ink-soft: rgba(255,255,255,0.9);
    --rule: rgba(255,255,255,0.55);
  }
  * { box-sizing: border-box; margin: 0; padding: 0; }
  html, body { width: 1200px; height: 999px; overflow: hidden; }
  body {
    position: relative;
    font-family: "Arimo", Arial, sans-serif;
    background: radial-gradient(ellipse 60% 60% at 50% 45%, var(--stage-center) 0%, var(--stage-center) 35%, var(--stage-edge) 100%);
  }
  .card {
    position: absolute;
    width: 581px;
    height: 335px;
    box-shadow: 2px 3px 6px rgba(0,0,0,0.35);
    color: var(--ink-light);
    overflow: hidden;
  }
  /* Front */
  .card-front {
    left: 309px; top: 109px;
    background: linear-gradient(to bottom, var(--slate) 0%, var(--slate) 58%, var(--slate-light) 61%, var(--slate) 66%, #383838 100%);
  }
  .brand {
    position: absolute;
    right: 290px;
    top: 182px;
    display: flex;
    align-items: center;
    gap: 10px;
  }
  .brand-dot {
    width: 16px; height: 16px;
    border-radius: 50%;
    background: var(--red-top);
  }
  .brand-name {
    font-size: 36px;
    font-weight: 700;
    color: var(--ink-light);
    letter-spacing: 0.5px;
  }
  .brand-divider {
    position: absolute;
    left: 307px; top: 168px;
    width: 1px; height: 64px;
    background: var(--rule);
  }
  .tagline {
    position: absolute;
    left: 329px; top: 193px;
    font-size: 14.5px;
    color: var(--ink-light);
  }
  /* Back */
  .card-back {
    top: 495px;
    background: linear-gradient(to bottom, var(--red-top) 0%, var(--red-bottom) 100%);
  }
  .card-back.left { left: 14px; }
  .card-back.right { left: 607px; }
  .contact-block {
    position: absolute;
    left: 307px; top: 128px;
  }
  .person-name {
    font-size: 33px;
    font-weight: 400;
    line-height: 1;
    margin-bottom: 16px;
  }
  .postal {
    font-size: 13px;
    line-height: 20px;
    color: var(--ink-soft);
    margin-bottom: 14px;
  }
  .location {
    font-size: 15.5px;
    font-weight: 700;
    line-height: 23px;
  }
  .contact-row {
    position: absolute;
    left: 12px; right: 14px; bottom: 10px;
    display: flex;
    justify-content: space-between;
    font-size: 14.5px;
  }
  .contact-item { display: flex; align-items: center; gap: 8px; }
  .contact-item svg { width: 17px; height: 12px; }
  .contact-item .sep { width: 1px; height: 12px; background: var(--ink-light); }
  .fax-tag {
    font-size: 8px;
    border: 1px solid var(--ink-light);
    padding: 0 2px;
    line-height: 10px;
  }
</style>
</head>
<body>

<section class="card card-front">
  <div class="brand">
    <span class="brand-dot"></span>
    <span class="brand-name">KESTRA</span>
  </div>
  <div class="brand-divider"></div>
  <p class="tagline">Bulk Heated Water</p>
</section>

<section class="card card-back left">
  <div class="contact-block">
    <h1 class="person-name">Dale Fenwick</h1>
    <p class="postal">Site 713, Box 2, Comp 4, RR3<br>Ashford Bend, XK, X9Z 4Q8</p>
    <p class="location">3-17-52-4 W4M<br>Hwy 905 Between RR37 &amp; RR38</p>
  </div>
  <div class="contact-row">
    <span class="contact-item">
      <svg viewBox="0 0 17 12" aria-hidden="true"><rect x="0.5" y="0.5" width="16" height="11" fill="none" stroke="#fff"/><path d="M0.5 0.5 L8.5 7 L16.5 0.5" fill="none" stroke="#fff"/></svg>
      <span class="sep"></span>info@kestraflowsupply.example</span>
    <span class="contact-item">
      <svg viewBox="0 0 17 12" aria-hidden="true"><path d="M1 4 Q8.5 -1 16 4 L14 5.5 L12 4 L12 3 Q8.5 2 5 3 L5 4 L3 5.5 Z" fill="#fff"/><rect x="4" y="6" width="9" height="5.5" rx="1" fill="none" stroke="#fff"/><circle cx="8.5" cy="8.7" r="1.4" fill="#fff"/></svg>
      <span class="sep"></span>555-318-2047</span>
    <span class="contact-item"><span class="fax-tag">Fax</span><span class="sep"></span>555-376-9150</span>
  </div>
</section>

<section class="card card-back right">
  <div class="contact-block">
    <h1 class="person-name">Dale Fenwick</h1>
    <p class="postal">Site 713, Box 2, Comp 4, RR3<br>Ashford Bend, XK, X9Z 4Q8</p>
    <p class="location">3-17-52-4 W4M<br>Hwy 905 Between RR37 &amp; RR38</p>
  </div>
  <div class="contact-row">
    <span class="contact-item">
      <svg viewBox="0 0 17 12" aria-hidden="true"><rect x="0.5" y="0.5" width="16" height="11" fill="none" stroke="#fff"/><path d="M0.5 0.5 L8.5 7 L16.5 0.5" fill="none" stroke="#fff"/></svg>
      <span class="sep"></span>info@kestraflowsupply.example</span>
    <span class="contact-item">
      <svg viewBox="0 0 17 12" aria-hidden="true"><path d="M1 4 Q8.5 -1 16 4 L14 5.5 L12 4 L12 3 Q8.5 2 5 3 L5 4 L3 5.5 Z" fill="#fff"/><rect x="4" y="6" width="9" height="5.5" rx="1" fill="none" stroke="#fff"/><circle cx="8.5" cy="8.7" r="1.4" fill="#fff"/></svg>
      <span class="sep"></span>555-318-2047</span>
    <span class="contact-item"><span class="fax-tag">Fax</span><span class="sep"></span>555-376-9150</span>
  </div>
</section>

</body>
</html>
```